Tallow Farm Brochure

To design a small brochure that tells people about our U-Pick cherry farm, where we are, when we are open and what our contact details are.

We have existing logo's which should be used. I have uploaded a file with these details.

Details about us are all located on:-
www.friendlink.example/tallowfarm
https://circlepage.example/u/0/b/704916382057419263851/704916382057419263851/about/p/pub

Farm

```html
<!DOCTYPE html>
<html lang="en">
<head>
<meta charset="utf-8">
<title>Tallow Farm – U Pick Cherries</title>
<link rel="stylesheet" href="https://fonts.googleapis.com/css2?family=Courgette&family=Montserrat:wght@400;500&display=swap">
<style>
  :root {
    --cherry-red: #d3273c;
    --cherry-deep: #b81f32;
    --cherry-soft: #e9a3ac;
    --leaf-green: #5b9a68;
    --leaf-light: #7fb48a;
    --paper: #ffffff;
    --ink: #3c3c3c;
  }
  html, body {
    margin: 0;
    padding: 0;
    overflow: hidden;
    background: var(--paper);
  }
  .brochure {
    position: relative;
    width: 802px;
    height: 1200px;
    overflow: hidden;
    background: var(--paper);
    font-family: "Montserrat", Arial, sans-serif;
  }
  .backdrop {
    position: absolute;
    inset: 0;
  }
  .cherries-art {
    position: absolute;
    left: 300px;
    top: 195px;
    width: 230px;
    height: 195px;
    background: linear-gradient(180deg, var(--cherry-soft) 0%, var(--cherry-red) 100%);
  }
  .title {
    position: absolute;
    top: 398px;
    left: 0;
    width: 100%;
    margin: 0;
    text-align: center;
    font-family: "Courgette", cursive;
    font-weight: 400;
    font-size: 84px;
    line-height: 1.2;
    color: var(--leaf-green);
  }
  .intro {
    position: absolute;
    top: 538px;
    left: 83px;
    width: 680px;
    margin: 0;
    font-size: 25.5px;
    line-height: 44px;
    color: var(--ink);
    white-space: nowrap;
  }
  .farm-name {
    position: absolute;
    top: 888px;
    left: 0;
    width: 100%;
    margin: 0;
    text-align: center;
    font-family: "Courgette", cursive;
    font-size: 66px;
    line-height: 1;
    color: var(--paper);
  }
  .address {
    position: absolute;
    top: 1046px;
    left: 0;
    width: 100%;
    margin: 0;
    text-align: center;
    font-size: 24px;
    color: var(--paper);
  }
  .hours {
    position: absolute;
    top: 1090px;
    left: 0;
    width: 100%;
    margin: 0;
    text-align: center;
    font-size: 33px;
    font-weight: 500;
    color: var(--paper);
  }
</style>
</head>
<body>
<main class="brochure">
  <svg class="backdrop" width="802" height="1200" viewBox="0 0 802 1200" aria-hidden="true">
    <polygon points="0,0 802,0 802,40 401,90 0,40" fill="var(--cherry-red)"/>
    <polygon points="620,0 802,0 802,30" fill="var(--cherry-deep)"/>
    <polygon points="0,30 401,78 802,30 802,62 401,122 0,62" fill="var(--leaf-green)"/>
    <polygon points="0,735 401,800 802,735 802,1200 0,1200" fill="var(--leaf-green)"/>
    <polygon points="0,742 401,808 802,742 802,752 401,818 0,752" fill="var(--leaf-light)"/>
    <polygon points="0,772 401,840 802,772 802,1200 0,1200" fill="var(--cherry-red)"/>
    <polygon points="0,772 170,801 0,1010" fill="var(--cherry-deep)"/>
    <polygon points="802,772 632,801 802,1010" fill="var(--cherry-deep)"/>
    <polygon points="0,1110 110,1200 0,1200" fill="var(--cherry-deep)"/>
    <polygon points="802,1090 680,1200 802,1200" fill="var(--cherry-deep)"/>
  </svg>

  <div class="cherries-art" role="img" aria-label="Illustration of a pair of red cherries on green stems"></div>

  <h1 class="title">U Pick Cherries</h1>

  <p class="intro">Tallow Farm is in the beautiful Yarra Valley,<br>an ideal location for growing sweet juicy cherries.<br>Visit us for Pick Your Own or Pre-Picked Cherries.</p>

  <p class="farm-name">Tallow<br>Farm</p>
  <p class="address">18 Ridgeline-Tallow Rd &nbsp;|&nbsp; Tallow, Victoria</p>
  <p class="hours">Friday-Sunday 10am-5pm</p>
</main>
</body>
</html>
```